Talvor GmbH business card

We Talvor GmbH based in Switzerland are looking for a business card design. The Fresh Jung, appealing to customers of all kinds. We already have a logo to upload but still a business card. Details: Talvor GmbH Address: Lindenweg 14b in 9476 Brugwil. Tel: 41 79 462 37 18, web: Talvor.ch, E-mail: info@Talvor.ch Facebook: Talvor GmbH. I am the Managing Director: Luka Petrovac. On reverse: Title: Transporter and bus rental Gross: Without deposit Super prices
Contact Information for Business Card
Siehe Projektbeschreibung
Requirements
Should not have
- Other pictures

```html
<!DOCTYPE html>
<html lang="de">
<head>
<meta charset="utf-8">
<title>Talvor GmbH – Visitenkarte</title>
<link href="https://fonts.googleapis.com/css2?family=Open+Sans:wght@400;600;700&display=swap" rel="stylesheet">
<style>
  :root {
    --navy: #24226a;
    --white: #ffffff;
    --steel: #7d9ab8;
    --backdrop: #e9e9ec;
    --shadow: rgba(0, 0, 0, 0.28);
  }
  * { box-sizing: border-box; margin: 0; padding: 0; }
  html, body {
    width: 1200px; height: 1000px; overflow: hidden;
    background: var(--backdrop);
    font-family: "Open Sans", Arial, sans-serif;
  }
  .card {
    position: absolute; left: 316px; width: 561px; height: 320px;
    border-radius: 24px; overflow: hidden;
    box-shadow: 3px 5px 8px var(--shadow);
  }
  .card-front { top: 172px; background: var(--navy); }
  .card-back  { top: 536px; background: var(--navy); }

  .front-header {
    position: absolute; left: 0; top: 0; width: 100%; height: 147px;
    background: var(--white);
  }
  .front-rule {
    position: absolute; left: 0; top: 152px; width: 100%; height: 1.5px;
    background: var(--white);
  }
  .wordmark {
    position: absolute; display: flex; align-items: center; gap: 14px;
    color: var(--navy); font-weight: 700; font-size: 54px; letter-spacing: 1px;
    white-space: nowrap;
  }
  .wordmark-square { width: 38px; height: 38px; background: var(--navy); }
  .card-front .wordmark { left: 66px; top: 44px; }
  .card-back .wordmark  { left: 92px; top: 140px; }

  .back-band {
    position: absolute; left: 0; top: 97px; width: 100%; height: 119px;
    background: var(--white);
  }
  .back-tagline {
    position: absolute; left: 0; width: 100%; top: 279px;
    text-align: center; color: var(--white); font-size: 13.5px;
  }

  .holder {
    position: absolute; left: 65px; top: 182px; color: var(--white);
  }
  .holder-icon { width: 24px; height: 24px; margin-bottom: 4px; }
  .holder-role { font-weight: 700; font-size: 13.5px; margin-bottom: 6px; }
  .holder-address { font-size: 13.5px; line-height: 18px; }

  .contact-list {
    position: absolute; left: 338px; top: 186px; list-style: none;
    color: var(--white); font-size: 13.5px;
  }
  .contact-list li {
    display: flex; align-items: center; gap: 11px; height: 24px;
  }
  .contact-list svg { width: 16px; height: 16px; flex: none; }
</style>
</head>
<body>

<section class="card card-front">
  <div class="front-header">
    <div class="wordmark"><span class="wordmark-square"></span>Talvor GmbH</div>
  </div>
  <div class="front-rule"></div>

  <div class="holder">
    <svg class="holder-icon" viewBox="0 0 24 24" fill="none" stroke="#fff" stroke-width="1.4" stroke-linejoin="round">
      <path d="M22 2 2 10l9 3 3 9z"/><path d="M22 2 11 13"/>
    </svg>
    <p class="holder-role">ich bin der geschaftsfuhrer</p>
    <p class="holder-address">Lindenweg 14b in<br>9476 Brugwil</p>
  </div>

  <ul class="contact-list">
    <li>
      <svg viewBox="0 0 24 24" fill="none" stroke="#fff" stroke-width="1.5" stroke-linejoin="round">
        <path d="M5 3h4l2 5-2.5 1.5a11 11 0 0 0 6 6L16 13l5 2v4a2 2 0 0 1-2 2A17 17 0 0 1 3 5a2 2 0 0 1 2-2z"/>
      </svg>+41 79 4623718</li>
    <li>
      <svg viewBox="0 0 24 24" fill="none" stroke="#fff" stroke-width="1.5">
        <rect x="2" y="5" width="20" height="14"/><path d="m2 5 10 8 10-8"/>
      </svg>info@Talvor.ch</li>
    <li>
      <svg viewBox="0 0 24 24" fill="none" stroke="#fff" stroke-width="1.4">
        <circle cx="12" cy="12" r="10"/><ellipse cx="12" cy="12" rx="4.5" ry="10"/><path d="M2 12h20M4 7h16M4 17h16"/>
      </svg>Talvor.ch</li>
    <li>
      <svg viewBox="0 0 24 24" fill="none" stroke="#fff" stroke-width="1.5">
        <circle cx="12" cy="12" r="10"/>
      </svg>Talvor Gmdh</li>
  </ul>
</section>

<section class="card card-back">
  <div class="back-band"></div>
  <div class="wordmark"><span class="wordmark-square"></span>Talvor GmbH</div>
  <p class="back-tagline">Transporter und Bus vermietung</p>
</section>

</body>
</html>
```